Maple's Pantry Home Page Design

Hello ArtHivePro -

I am looking for a home page design for an Indian Food Grocery ecommerce site with a store in Boulder, CO. This design request is just for the home page (http://maplespantry.com/), including new design, font, layout and emblem/word mark logo.

What: Maple's Pantry (spices, lentils, rice, frozen foods, etc.)

Desired Color Scheme: Warm, earth tones (red, orange, yellow), that remind the guest of Indian Spices

Tone: This is an Indian-American family owned, small business catering imported Indian foods and spices to a primary market of Indian-Americans and a secondary market of Indian food/spice lovers.

Themes to communicate: Indian, family owned, food

Sample Websites: http://www.brivantfare.com/, http://www.tolvacart.com/, http://www.quenlarmart.com/

Please feel free to reach out with any questions. Thank you.

Target Market(s)

Indian-Americans (1st and 2nd Generation)

Industry/Entity Type

Small Business

Requirements
Must have
• Final Design must be delivered in layered PSD file with all fonts and licenses used.

```html
<!DOCTYPE html>
<html lang="en">
<head>
<meta charset="utf-8">
<title>Maple's Pantry – Home</title>
<link href="https://fonts.googleapis.com/css2?family=Dancing+Script:wght@700&family=Open+Sans:wght@400;600;700&display=swap" rel="stylesheet">
<style>
:root{
  --wood-dark:#231a12;
  --wood-mid:#3a2b1e;
  --wood-light:#4a3727;
  --orange:#d9731a;
  --orange-light:#f0a030;
  --orange-deep:#b8570c;
  --paper:#ffffff;
  --ink:#444;
  --ink-soft:#777;
  --footer:#221a14;
  --footer-text:#cfc6bb;
  --news-bg:#3d3128;
}
*{margin:0;padding:0;box-sizing:border-box}
html,body{width:872px;height:1200px;overflow:hidden}
body{
  position:relative;
  font-family:'Open Sans',Arial,sans-serif;
  color:var(--ink);
  background:linear-gradient(90deg,var(--wood-dark),var(--wood-mid) 30%,var(--wood-light) 50%,var(--wood-mid) 70%,var(--wood-dark));
}
.script{font-family:'Dancing Script',cursive;font-weight:700}

/* header */
.site-header{position:absolute;left:116px;top:0;width:646px;height:87px}
.brand{position:absolute;left:6px;top:18px;color:#fff;font-size:36px;display:flex;align-items:center;gap:10px}
.brand-dot{width:14px;height:14px;border-radius:50%;background:var(--orange)}
.cart{position:absolute;right:0;top:10px;width:166px;height:54px;background:#2a211a;border:1px solid #5a4634;border-radius:4px;display:flex;align-items:center;gap:10px;padding:0 10px}
.cart svg{flex:none}
.cart-title{color:#fff;font-size:13px;font-weight:600}
.cart-meta{color:#bbb;font-size:10px;display:flex;justify-content:space-between;width:96px;margin-top:2px}

/* nav */
.main-nav{position:absolute;left:116px;top:87px;width:646px;height:38px;background:linear-gradient(var(--orange-light),var(--orange-deep));display:flex;align-items:center;justify-content:space-around;padding:0 6px}
.main-nav a{color:#fff;text-decoration:none;font-size:21px}

/* slider */
.slider{position:absolute;left:116px;top:125px;width:646px;height:292px;background:var(--paper);display:flex;gap:6px}
.slide{flex:1;height:100%}
.slide-1{background:linear-gradient(160deg,#8a5a2a,#c97b34 45%,#e8c79a)}
.slide-2{background:linear-gradient(150deg,#f2ece4,#c58a4a 50%,#6e3b18)}
.slide-3{background:linear-gradient(140deg,#7a4a1e,#d99a40 50%,#a8652a)}
.slider-arrow{position:absolute;top:128px;width:30px;height:34px;background:rgba(255,255,255,.9);display:flex;align-items:center;justify-content:center}
.slider-arrow.prev{left:0}
.slider-arrow.next{right:0}

.wood-band{position:absolute;left:0;top:417px;width:872px;height:46px;background:linear-gradient(#150f0a,#2e2217)}

/* content */
.content{position:absolute;left:116px;top:417px;width:646px;height:627px;background:var(--paper)}
.welcome-title{position:absolute;left:14px;top:16px;color:var(--orange);font-size:30px}
.welcome-text{position:absolute;left:14px;top:64px;width:400px;font-size:10.5px;line-height:16px;color:var(--ink-soft)}
.welcome-photo{position:absolute;left:14px;top:114px;width:400px;height:152px;background:radial-gradient(ellipse at 55% 55%,#f0d9a0,#d9a04a 45%,#7a4a22 80%)}
.chef-photo{position:absolute;left:436px;top:14px;width:196px;height:158px;background:linear-gradient(160deg,#3a2d24,#b8a590 50%,#f2eee8)}
.chef-name{position:absolute;left:436px;top:180px;font-size:14px;font-weight:700;color:var(--orange)}
.chef-text{position:absolute;left:436px;top:202px;width:196px;font-size:10px;line-height:15px;color:var(--ink-soft)}

.products-title{position:absolute;left:14px;top:282px;color:var(--orange);font-size:30px}
.products{position:absolute;left:14px;top:338px;width:620px;display:grid;grid-template-columns:repeat(3,1fr);row-gap:18px;column-gap:16px}
.product{display:flex;gap:10px;height:88px}
.product-photo{width:90px;height:88px;flex:none}
.product h3{font-size:14px;font-weight:700;color:var(--orange);margin-top:6px}
.product p{font-size:9.5px;line-height:13px;color:var(--ink-soft);margin-top:3px}
.read-more{display:inline-block;margin-top:8px;background:var(--orange);color:#fff;font-size:9px;padding:3px 10px;border-radius:2px}
.pp-1{background:linear-gradient(135deg,#b0501a,#e39a3a)}
.pp-2{background:linear-gradient(135deg,#6e2d12,#d07a30)}
.pp-3{background:linear-gradient(135deg,#7a3a1a,#e0b060)}
.pp-4{background:linear-gradient(135deg,#c87a2a,#f0d8a0)}
.pp-5{background:linear-gradient(135deg,#e6e0d0,#b89a6a)}
.pp-6{background:linear-gradient(135deg,#8a3a1a,#f0c070)}

/* footer */
.site-footer{position:absolute;left:0;top:1044px;width:872px;height:156px;background:var(--footer)}
.footer-col{position:absolute;top:16px;color:var(--footer-text)}
.footer-col h4{font-size:13px;font-weight:600;color:#fff;margin-bottom:6px}
.footer-col li{list-style:none;font-size:10px;line-height:17px}
.col-appetizers{left:116px}
.col-soups{left:276px}
.newsletter{position:absolute;left:440px;top:14px;width:322px;height:94px;background:var(--news-bg);text-align:center;padding-top:8px}
.newsletter h4{color:#fff;font-size:26px}
.newsletter-input{margin:6px auto 0;width:200px;height:20px;background:#fff;font-size:9px;color:#999;text-align:left;padding:4px 8px}
.signup{display:inline-block;margin-top:8px;background:linear-gradient(var(--orange-light),var(--orange-deep));color:#fff;font-size:12px;padding:4px 26px;border-radius:3px}
.copyright{position:absolute;left:116px;bottom:14px;font-size:9px;color:#a89c8f}
</style>
</head>
<body>

<header class="site-header">
  <div class="brand script"><span class="brand-dot"></span>Maple's Pantry</div>
  <div class="cart">
    <svg width="30" height="26" viewBox="0 0 30 26"><path d="M2 3h5l4 14h14l3-10H9" fill="none" stroke="#f0a030" stroke-width="2.4" stroke-linejoin="round"/><circle cx="12" cy="22" r="2.4" fill="#f0a030"/><circle cx="23" cy="22" r="2.4" fill="#f0a030"/></svg>
    <div>
      <div class="cart-title">Shopping Cart</div>
      <div class="cart-meta"><span>0 items</span><span>$0.00</span></div>
    </div>
  </div>
</header>

<nav class="main-nav script">
  <a href="#">Home</a><a href="#">About</a><a href="#">Drinks and More</a><a href="#">Dry Fruits</a><a href="#">Rice</a><a href="#">Noodles</a><a href="#">Contact</a>
</nav>

<div class="wood-band"></div>

<section class="slider">
  <div class="slide slide-1" role="img" aria-label="Plated Indian curry with rice and bread"></div>
  <div class="slide slide-2" role="img" aria-label="Spoons of ground spices on a white table"></div>
  <div class="slide slide-3" role="img" aria-label="Spiced roasted potatoes in a bowl"></div>
  <span class="slider-arrow prev"><svg width="14" height="16" viewBox="0 0 14 16"><path d="M11 1L3 8l8 7" fill="none" stroke="#555" stroke-width="3"/></svg></span>
  <span class="slider-arrow next"><svg width="14" height="16" viewBox="0 0 14 16"><path d="M3 1l8 7-8 7" fill="none" stroke="#555" stroke-width="3"/></svg></span>
</section>

<main class="content">
  <h1 class="welcome-title script">Welcome to our Grocery Store</h1>
  <p class="welcome-text">Our family has brought the flavours of home to Boulder for many years. Browse whole and ground spices, fragrant basmati rice, lentils, snacks and frozen meals, all chosen with care and packed fresh for your kitchen every week.</p>
  <div class="welcome-photo" role="img" aria-label="Large platter of Indian dishes with rice and sweets"></div>

  <div class="chef-photo" role="img" aria-label="Portrait of the store chef"></div>
  <div class="chef-name">Priya Nandan – Chef</div>
  <p class="chef-text">Our chef shares simple recipes each month using the spices on our shelves. Stop by the store to taste a new dish and ask for cooking tips.</p>

  <h2 class="products-title script">Our Latest Products</h2>
  <div class="products">
    <article class="product"><div class="product-photo pp-1" role="img" aria-label="Bowl of mild spice blend"></div><div><h3>Mild Spice</h3><p>Gentle warmth, everyday cooking</p><span class="read-more">Read More</span></div></article>
    <article class="product"><div class="product-photo pp-2" role="img" aria-label="Dish of red chilli spices"></div><div><h3>Spicy</h3><p>Bold heat, rich colour</p><span class="read-more">Read More</span></div></article>
    <article class="product"><div class="product-photo pp-3" role="img" aria-label="Prepared Indian meal"></div><div><h3>Our Food</h3><p>Frozen meals, ready fast</p><span class="read-more">Read More</span></div></article>
    <article class="product"><div class="product-photo pp-4" role="img" aria-label="Assorted Indian snacks"></div><div><h3>Indian Charm</h3><p>Classic snacks, family favourites</p><span class="read-more">Read More</span></div></article>
    <article class="product"><div class="product-photo pp-5" role="img" aria-label="Bowl of basmati rice"></div><div><h3>Rice</h3><p>Long grain, aged basmati</p><span class="read-more">Read More</span></div></article>
    <article class="product"><div class="product-photo pp-6" role="img" aria-label="Fresh vegetables and lentils"></div><div><h3>Freshness</h3><p>Fresh stock, great price</p><span class="read-more">Read More</span></div></article>
  </div>
</main>

<footer class="site-footer">
  <div class="footer-col col-appetizers">
    <h4>Appetizers</h4>
    <ul><li>Saffron Lamb Masala</li><li>Kebab Sampler</li><li>Hariyali Shrimp</li><li>Samosa Chaat</li><li>Vegetable Pakora</li></ul>
  </div>
  <div class="footer-col col-soups">
    <h4>Soups and Salads</h4>
    <ul><li>Mulligatawny Soup</li><li>Murg Tomato Shorba</li><li>Kachumber Salad</li><li>Mixed Garden Salad</li><li>Lentil Salad</li></ul>
  </div>
  <div class="newsletter">
    <h4 class="script">Newsletter</h4>
    <div class="newsletter-input">Your email address</div>
    <span class="signup">Sign up</span>
  </div>
  <p class="copyright">2013 Maple's Pantry 2013 Copyright All Rights Reserved</p>
</footer>

</body>
</html>
```